Executive search firm in fashion, luxury and retail industry needs logo and card design.

We are a start-up recruiting firm that specializes in the retail and fashion industry, based in New York. We are looking for something that will appeal to CEO level clients and candidates, but that has a little design edge...not overly corporate but still CEO-appropriate. We have clean, sophisticated taste and want a contemporary feel. Happy to have a two sided card. Not afraid of a little color but it should be high-design, not gimmicky and tasteful.

Quillmart Market(s)

CEO's, HR Leaders, in retail, fashion (i.e. Halvorsen, Quillmart, Otto Brevik)

Industry/Entity Type

Professional Service

Contact Information for Business Card

Calloway Ridge Search Partners
Address to be determined
Marrowfield, ST 00421

Marta Velard
Managing Director
(555)038-4172
mvelard@callowayridgesearch.example

Font styles to use
Serif
Sans Serif

Requirements
Must have
• clean lines, crisp graphics, some color. Prefer a graphic treatment over a "logo" per se. No pictures, etc.
Nice to have
• double sided design.
Should not have
• Gimmicks, smaltz, goop. Think Gallery of Current Works, not the Dunmore Holdings. No earth tones, as in beige and brown, no pastels. Strong colors are fine in moderation. Grays are good. Jewel tones are good. No red.

```html
<!DOCTYPE html>
<html lang="en">
<head>
<meta charset="utf-8">
<title>Calloway Ridge Search Partners — Identity</title>
<link rel="stylesheet" href="https://fonts.googleapis.com/css2?family=Questrial&display=swap">
<style>
  :root {
    --page: #ececec;
    --ink: #3a3a3a;
    --ink-soft: #6f6f6f;
    --card-dark: #1c1c1e;
    --card-dark-edge: #2a2a2d;
    --card-light: #fbfbfb;
    --accent: #2a8fd6;
    --accent-deep: #1d5f95;
    --white: #ffffff;
    --logo-ink: #222222;
  }
  * { box-sizing: border-box; margin: 0; padding: 0; }
  html, body { width: 1200px; height: 2290px; overflow: hidden; }
  body {
    background: var(--page);
    font-family: "Questrial", "Century Gothic", sans-serif;
    color: var(--ink);
    position: relative;
  }
  .card {
    position: absolute;
    left: 120px;
    width: 960px;
    height: 549px;
    border-radius: 6px;
    box-shadow: 0 18px 40px rgba(0,0,0,0.18);
    overflow: hidden;
  }
  .brand { display: flex; align-items: center; }
  .brand-dot { border-radius: 50%; background: var(--accent); flex: none; }
  .brand-name { line-height: 1.1; letter-spacing: 0.5px; white-space: nowrap; }

  /* Front side */
  .card--front {
    top: 200px;
    background: linear-gradient(135deg, var(--card-dark-edge) 0%, var(--card-dark) 55%, #111113 100%);
  }
  .card--front .accent-line {
    position: absolute;
    left: 770px;
    top: 0;
    width: 4px;
    height: 100%;
    background: var(--accent);
  }
  .card--front .brand { position: absolute; left: 170px; top: 228px; gap: 22px; }
  .card--front .brand-dot { width: 40px; height: 40px; }
  .card--front .brand-name { font-size: 42px; color: var(--white); }

  /* Back side */
  .card--back {
    top: 1150px;
    background: linear-gradient(160deg, var(--white) 0%, var(--card-light) 60%, #f0f0f0 100%);
  }
  .card--back .contact { position: absolute; left: 470px; top: 110px; }
  .person-name { font-size: 40px; color: var(--ink); letter-spacing: 0.5px; }
  .person-title { font-size: 24px; color: var(--accent); margin-top: 6px; margin-bottom: 30px; }
  .contact-list { list-style: none; }
  .contact-item {
    display: flex;
    align-items: center;
    gap: 16px;
    font-size: 22px;
    color: var(--ink-soft);
    margin-bottom: 16px;
  }
  .contact-icon { width: 22px; height: 22px; flex: none; }
  .card--back .brand { position: absolute; left: 70px; bottom: 70px; gap: 16px; }
  .card--back .brand-dot { width: 26px; height: 26px; }
  .card--back .brand-name { font-size: 28px; color: var(--ink); }

  /* Standalone lockup */
  .identity {
    position: absolute;
    left: 0;
    top: 1900px;
    width: 1200px;
    height: 390px;
    background: var(--white);
    display: flex;
    align-items: center;
    justify-content: center;
  }
  .identity .brand { gap: 30px; }
  .identity .brand-dot { width: 56px; height: 56px; background: var(--accent-deep); }
  .identity .brand-name { font-size: 62px; color: var(--logo-ink); }
</style>
</head>
<body>

  <section class="card card--front" aria-label="Business card front">
    <div class="accent-line"></div>
    <div class="brand">
      <span class="brand-dot"></span>
      <span class="brand-name">Calloway Ridge<br>Search Partners</span>
    </div>
  </section>

  <section class="card card--back" aria-label="Business card back">
    <div class="contact">
      <p class="person-name">Marta Velard</p>
      <p class="person-title">Managing Director</p>
      <ul class="contact-list">
        <li class="contact-item">
          <svg class="contact-icon" viewBox="0 0 24 24" aria-hidden="true">
            <rect x="1" y="1" width="22" height="22" rx="4" fill="var(--accent)"/>
            <path d="M7 6c1 0 1.5 2.5 1 3.3-.4.6-.9.7-.5 1.5.8 1.5 2.2 2.9 3.7 3.7.8.4.9-.1 1.5-.5.8-.5 3.3 0 3.3 1s-1 2.5-2.5 2.5C8.8 17.5 6.5 12 6.5 8.5 6.5 7 6.3 6 7 6z" fill="var(--white)"/>
          </svg>
          <span>(555)038-4172</span>
        </li>
        <li class="contact-item">
          <svg class="contact-icon" viewBox="0 0 24 24" aria-hidden="true">
            <rect x="1" y="1" width="22" height="22" rx="4" fill="var(--accent)"/>
            <rect x="5" y="7" width="14" height="10" fill="none" stroke="var(--white)" stroke-width="1.6"/>
            <path d="M5 7l7 6 7-6" fill="none" stroke="var(--white)" stroke-width="1.6"/>
          </svg>
          <span>mvelard@callowayridgesearch.example</span>
        </li>
        <li class="contact-item">
          <svg class="contact-icon" viewBox="0 0 24 24" aria-hidden="true">
            <circle cx="12" cy="12" r="11" fill="var(--accent)"/>
            <path d="M12 5a4.5 4.5 0 0 0-4.5 4.5C7.5 13 12 18.5 12 18.5s4.5-5.5 4.5-9A4.5 4.5 0 0 0 12 5z" fill="var(--white)"/>
            <circle cx="12" cy="9.5" r="1.7" fill="var(--accent)"/>
          </svg>
          <span>Marrowfield, ST 00421</span>
        </li>
      </ul>
    </div>
    <div class="brand">
      <span class="brand-dot"></span>
      <span class="brand-name">Calloway Ridge Search Partners</span>
    </div>
  </section>

  <section class="identity" aria-label="Brand name lockup">
    <div class="brand">
      <span class="brand-dot"></span>
      <span class="brand-name">Calloway Ridge<br>Search Partners</span>
    </div>
  </section>

</body>
</html>
```